HTML Web layout / data visualization for an information software application

We have a product used by patent analysts to allow them examine information stored in patents - particularly those patents that include biological sequences like DNA, RNA, and protein.

When the user opens up a particular patent, they currently see a very poorly organized wall of text, presenting fields of data to them in unorganized ways. We have attached screenshots of the current interface.

The project is to redesign that layout so that the same information is presented in a way which is brings important data to the the eyes of the user, categorizes data appropriately, and is visually appealing. We have proposed logical categorizations of data in the document called "Fields documentation."

The deliverable should be an HTML5 file that renders one or more of the examples of records we've provided in your new design.

Description of files:

"Examples of records badly displayed": MS Word file that shows three different examples of the records we would like to better visualize.

"screengrab1.tiff" and "screengrab2.tiff": pictures of how these records sit inside of our product. This is presented to give you a sense of screen real estate, our look and feel, and colors. We do not want the whole screen redesigned - just the record display itself.

"Fields documentation": detailed documentation of what each field means. We have tried to group them logically for you, and have also attempted to inform you as to which fields are linked to others.

Hi all,

Thanks for the designs so far. Unfortunately, nearly every design fails to understand the nature of the project. The problem we have is not about fonts and colors (although those matter). It is about grouping information together and displaying data in a way that provides insight. In the original brief, we say:

The document we have uploaded called "Fields documentation" is the most important document. We sense that very few of you have taken it into account. It provides notes on the nature of the data in the report and gives signs of the ways in which a creative designer might help to arrange the content.

Thanks for your consideration of this project.

TM

Target Market(s)

Patent analysts, heavily educated scientists, Ph.Ds.

Industry/Entity Type

Software

```html
<!DOCTYPE html>
<html lang="en">
<head>
<meta charset="utf-8">
<title>TM pat Gold Nucleotide – patent sequences</title>
<link href="https://fonts.googleapis.com/css2?family=Source+Sans+3:wght@400;600&display=swap" rel="stylesheet">
<style>
:root{
  --ink:#2b2b2b;
  --muted:#555;
  --link:#1f8ac0;
  --brand:#1c8fc9;
  --accent:#d0211b;
  --bar:#5f6a70;
  --bar-text:#f1f3f4;
  --line:#d4d7d9;
  --panel:#f3f4f5;
  --label-bg:#f2f2f2;
  --header-bg:#efefef;
}
*{box-sizing:border-box;margin:0;padding:0}
html,body{width:1200px;height:1055px;overflow:hidden;background:#fff}
body{position:relative;font-family:"Source Sans 3",sans-serif;font-size:12.5px;color:var(--ink)}
a{color:var(--link);text-decoration:none}
.abs{position:absolute}

.site-header{left:0;top:0;width:1200px;height:75px;background:var(--header-bg)}
.brand{left:42px;top:22px;display:flex;align-items:center;gap:8px;font-size:24px;font-weight:600;color:var(--brand)}
.brand-dot{width:26px;height:26px;border-radius:50%;background:var(--brand)}
.top-nav{right:42px;top:31px;display:flex;gap:17px;font-size:12px}
.caret{display:inline-block;width:0;height:0;border-left:4px solid transparent;border-right:4px solid transparent;border-top:4px solid currentColor;margin-left:4px;vertical-align:middle}

.breadcrumb{left:39px;top:84px;font-size:12.5px;font-weight:600}
.breadcrumb a{margin-left:6px}

.toolbar{left:39px;top:117px;width:1120px;height:118px;background:var(--panel);border:1px solid var(--line);border-radius:3px;overflow:hidden}
.menu-bar{height:35px;background:var(--bar);color:var(--bar-text);display:flex;align-items:center;padding:0 24px;gap:31px;font-size:13px}
.menu-bar .selected{margin-left:auto}
.menu-bar .selected b{color:#4fb6e8;margin-left:6px}
.tool-btn{top:56px;height:42px;display:flex;align-items:center;gap:10px;padding:0 14px;border:1px solid #ccc;border-radius:2px;background:#f7f7f7;font-size:12.5px;font-weight:600;letter-spacing:.3px;color:#999}
.tool-btn.active{border-color:#9aa0a4;background:#fff;color:#333;box-shadow:inset 0 0 0 1px #e6e6e6}
.tool-btn svg{width:24px;height:22px}

.pager-note{left:39px;top:254px}
.pager{left:408px;top:254px;display:flex;gap:18px}
.pager .count{color:var(--ink);font-weight:600}
.pager .count em{font-style:normal;color:var(--accent)}
.patent-view{right:41px;top:254px;color:var(--accent);font-weight:600}

.results{left:39px;top:281px;width:1120px;border:1px solid var(--line);border-radius:3px;overflow:hidden}
.results-row{display:grid;grid-template-columns:37px 134px 105px 232px 143px 108px 132px 112px 117px}
.results-head{background:var(--bar);color:var(--bar-text);font-weight:600;font-size:12px;height:52px}
.results-head>div{padding:14px 9px 0;border-left:1px solid #7b858a}
.results-head>div:first-child{border-left:0;padding:10px 0 0 12px}
.results-body{height:27px;align-items:center;font-size:12px;border-top:1px solid var(--line)}
.results-body>div{padding:0 9px;height:100%;display:flex;align-items:center;border-left:1px solid var(--line);white-space:nowrap}
.results-body>div:first-child{border-left:0;padding-left:12px}
.checkbox{width:13px;height:13px;border:1px solid #8a9399;background:#fff}
.checkbox.on{background:#1d6fa5;border-color:#0e3e5e}

.tabs{left:39px;top:404px;display:flex;gap:0}
.tab{height:37px;padding:0 18px;display:flex;align-items:center;font-size:15px;border:1px solid var(--line);border-bottom:0;border-radius:3px 3px 0 0}
.tab.patent{width:127px;background:var(--panel);justify-content:center}
.tab.length{background:var(--brand);color:#fff;border-color:var(--brand);margin-left:-24px;position:relative}
.close-link{font-size:12.5px;color:#444}
.close-top{right:41px;top:417px}

.detail-panel{left:39px;top:440px;width:1120px;height:572px;background:var(--panel);border:1px solid var(--line);border-radius:0 3px 3px 3px}
.detail{position:absolute;left:12px;top:13px;width:1096px;height:525px;background:#fff;border:1px solid var(--line)}
.detail-label-col{position:absolute;left:0;top:0;width:185px;height:100%;background:var(--label-bg)}
.field{position:absolute;left:0;width:100%;border-bottom:1px solid var(--line);display:flex}
.field .label{width:185px;padding:8px 13px 0;line-height:1.45}
.field .label small{font-size:11px;color:var(--muted)}
.field .value{padding:8px 20px 0}
.claims-title{color:var(--link);font-weight:600;letter-spacing:.3px;margin-bottom:7px}
.claims p{line-height:19.5px;font-size:12.3px;width:875px}
.close-bottom{right:12px;bottom:-1px}
.copyright{left:40px;top:1024px;font-size:11.5px;color:#444}
</style>
</head>
<body>

<header class="site-header abs">
  <div class="brand abs"><span class="brand-dot"></span>SeqVista</div>
  <nav class="top-nav abs">
    <a href="#">Adminstration</a>
    <a href="#">Quick Launch<span class="caret"></span></a>
    <a href="#">Help<span class="caret"></span></a>
    <a href="#">Help on this page</a>
  </nav>
</header>

<div class="breadcrumb abs">Home &nbsp;&gt;<a href="#">TM pat Gold Nucleotide- patent sequences</a></div>

<section class="toolbar abs">
  <div class="menu-bar">
    <span>Result</span><span>View</span><span>Export</span><span>Applications</span>
    <span class="selected">0 result selected<b>x</b></span>
  </div>
  <div class="tool-btn active abs" style="left:24px">
    <svg viewBox="0 0 24 22"><rect x="1" y="2" width="20" height="17" fill="#fff" stroke="#555"/><line x1="1" y1="7" x2="21" y2="7" stroke="#555"/><line x1="4" y1="11" x2="12" y2="11" stroke="#888"/><line x1="4" y1="14" x2="10" y2="14" stroke="#888"/><circle cx="16" cy="14" r="3.5" fill="none" stroke="#333" stroke-width="1.5"/><line x1="18.5" y1="16.5" x2="22" y2="20" stroke="#333" stroke-width="2"/></svg>
    FILTERING<span class="caret" style="color:#333"></span>
  </div>
  <div class="tool-btn abs" style="left:181px">
    <svg viewBox="0 0 24 22"><ellipse cx="12" cy="5" rx="8" ry="3" fill="#ddd" stroke="#aaa"/><path d="M4 5v12c0 1.7 3.6 3 8 3s8-1.3 8-3V5" fill="#e6e6e6" stroke="#aaa"/><path d="M4 11c0 1.7 3.6 3 8 3s8-1.3 8-3" fill="none" stroke="#aaa"/></svg>
    GROUPING<span class="caret"></span>
  </div>
  <div class="tool-btn abs" style="left:338px">
    <svg viewBox="0 0 24 22"><path d="M6 2v15M2 13l4 5 4-5" fill="none" stroke="#7aa6c7" stroke-width="2"/><text x="13" y="9" font-size="9" fill="#999" font-family="sans-serif">A</text><text x="13" y="20" font-size="9" fill="#999" font-family="sans-serif">Z</text></svg>
    SORTING<span class="caret"></span>
  </div>
</section>

<div class="pager-note abs">Result are Ungrouped, Filter Applied</div>
<div class="pager abs">
  <a href="#">&lt;&lt; First</a><a href="#">&lt; &nbsp;Prev</a>
  <span class="count">Sequences 1-50 of <em>936, &nbsp;432</em></span>
  <a href="#">Next &gt; &nbsp;Last &gt;&gt;</a>
</div>
<div class="patent-view abs">Patent View</div>

<section class="results abs">
  <div class="results-row results-head">
    <div><div class="checkbox on"></div><div class="checkbox" style="margin-top:7px"></div></div>
    <div>Identifier</div><div>Patent Assignee</div><div>Patent Title</div><div>Extended Legal Status</div>
    <div>Publication Date</div><div>Earliest Priority Date</div><div>Patent Sequence Location</div><div>PCT Pub. Date <span class="caret"></span></div>
  </div>
  <div class="results-row results-body" style="height:34px">
    <div><div class="checkbox"></div></div>
    <div><a href="#">WO2012054321</a>-0001</div><div>KIM, ET, AL;</div><div>Polycomb Associated Non Coding RNAS</div><div>PENDING</div>
    <div>29June 2013</div><div>29June 2013</div><div>29June 2013</div><div>0</div>
  </div>
  <div class="results-row results-body">
    <div></div>
    <div><a href="#">WO2012054321</a>-0001</div><div>KIM, ET, AL;</div><div>Polycomb Associated Non Coding RNAS</div><div>PENDING</div>
    <div>29June 2013</div><div>29June 2013</div><div>29June 2013</div><div>0</div>
  </div>
</section>

<div class="tabs abs">
  <div class="tab patent">Patent</div>
  <div class="tab length">Sequence Length: 467,413</div>
</div>
<a class="close-link close-top abs" href="#">[ Close ]</a>

<section class="detail-panel abs">
  <div class="detail">
    <div class="detail-label-col"></div>
    <div class="field" style="top:0;height:35px"><div class="label">Identifier</div><div class="value"><a href="#">WO2012054321</a>-0001</div></div>
    <div class="field" style="top:35px;height:30px"><div class="label">Patent Sequence Location</div><div class="value">Claim: 1</div></div>
    <div class="field" style="top:65px;height:48px"><div class="label">Organism<br><small>(Non-Normalized Name)</small></div><div class="value">Mus Musculus</div></div>
    <div class="field" style="top:113px;height:28px"><div class="label">Organism</div><div class="value">Mus Musculus ( house mouse )</div></div>
    <div class="field" style="top:141px;height:30px"><div class="label">Taxonomy ID</div><div class="value">10090</div></div>
    <div class="field" style="top:171px;height:29px"><div class="label">Patent SEQ ID No.</div><div class="value">2</div></div>
    <div class="field claims" style="top:200px;border-bottom:0"><div class="label">Claims</div>
      <div class="value">
        <div class="claims-title">WHAT IS CLAIMED IS:</div>
        <p>Aliquam molestie, mi et imperdiet euismod, dui purus auctor tellus, et interdum lacus lectus et ante. Sed accumsan sollicitudin sapien, sit amet adipiscing turpis gravida ac. In congue, neque ac lobortis volutpat, libero mauris varius mi, vitae suscipit ipsum ligula vitae risus. Duis aliquam nibh a dui iaculis viverra id a velit. Vivamus egestas risus in magna varius commodo. Sed semper viverra egestas. Etiam pretium porttitor lectus, vel ornare neque porta volutpat.</p>
        <p>Vestibulum ante ipsum primis in faucibus orci luctus et ultrices posuere cubilia Curae; Ut et scelerisque ante. Donec erat purus, faucibus vitae congue vel, porttitor nec lectus. Aenean a nibh eget turpis vehicula tempus ac sed massa. Vestibulum dolor nulla, ultrices ac tincidunt sed, laoreet non est. Suspendisse lobortis turpis in odio blandit ac interdum lorem euismod. Etiam risus massa, vulputate eu pellentesque et, consectetur a neque.</p>
        <p>Aliquam molestie, mi et imperdiet euismod, dui purus auctor tellus, et interdum lacus lectus et ante. Sed accumsan sollicitudin sapien, sit amet adipiscing turpis gravida ac. In congue, neque ac lobortis volutpat, libero mauris varius mi, vitae suscipit ipsum ligula vitae risus. Duis aliquam nibh a dui iaculis viverra id a velit. Vivamus egestas risus in magna varius commodo. Sed semper viverra egestas. Etiam pretium porttitor lectus, vel ornare neque porta volutpat.</p>
        <p>Vestibulum ante ipsum primis in faucibus orci luctus et ultrices posuere cubilia Curae; Ut et scelerisque ante. Donec erat purus, faucibus vitae congue vel, porttitor nec lectus. Aenean a nibh eget turpis vehicula tempus ac sed massa. Vestibulum dolor nulla, ultrices ac tincidunt sed, laoreet non est. Suspendisse lobortis turpis in odio blandit ac interdum lorem euismod. Etiam risus massa, vulputate eu pellentesque et, consectetur a neque.</p>
      </div>
    </div>
  </div>
  <a class="close-link close-bottom abs" href="#" style="bottom:-5px;right:12px;top:549px">[ Close ]</a>
</section>

<div class="copyright abs">Copyright (c) SeqVista, Inc &nbsp;2013</div>

</body>
</html>
```